Retail Seafood business needs package/label design

In need of packaging/label design for multiple seafood products such as sword fish, halibut, cod fish, scallops, mahi, catfish, and lobster tails

```html
<!DOCTYPE html>
<html lang="en">
<head>
<meta charset="utf-8">
<title>Lobster Tails Label</title>
<link rel="stylesheet" href="https://fonts.googleapis.com/css2?family=Italiana&family=Allura&family=Arimo&display=swap">
<style>
  :root {
    --bg: #586d7b;
    --paper: #f1f2f3;
    --navy: #0d4a6e;
    --sky: #86c6e8;
    --cream: #ece3d3;
    --ink: #1d2b36;
    --sketch: #dfe6ec;
  }
  * { margin: 0; padding: 0; box-sizing: border-box; }
  html, body { width: 1200px; height: 800px; overflow: hidden; }
  body { background: var(--bg); position: relative; }

  .label {
    position: absolute; left: 330px; top: 10px;
    width: 540px; height: 780px;
    background: var(--paper);
  }
  .brand-band {
    position: absolute; left: 0; top: 43px; width: 100%; height: 132px;
    background: var(--navy);
    display: flex; align-items: center; justify-content: center;
  }
  .brand-name {
    font-family: "Italiana", serif;
    font-size: 40px; color: var(--cream); letter-spacing: 2px;
  }
  .title-box {
    position: absolute; left: 0; top: 260px; width: 240px; height: 262px;
    background: var(--navy);
    padding: 22px 0 0 40px;
    font-family: "Italiana", serif;
  }
  .product-name {
    color: #ffffff; font-size: 66px; line-height: 68px; font-weight: 400;
  }
  .origin {
    color: var(--sky); font-size: 44px; line-height: 60px; margin-top: 8px;
  }
  .illustration {
    position: absolute; left: 267px; top: 225px; width: 273px; height: 325px;
    background: radial-gradient(ellipse at 55% 50%, #c9d7e3 0%, var(--paper) 72%);
  }
  .badges { position: absolute; left: 0; top: 0; }
  .badge {
    position: absolute; width: 88px; height: 88px; border-radius: 50%;
    border: 1.5px solid var(--ink);
    display: flex; align-items: center; justify-content: center; text-align: center;
    font-family: "Allura", cursive; font-size: 24px; line-height: 24px; color: var(--ink);
  }
  .badge--fresh { left: 103px; top: 576px; }
  .badge--quality { left: 208px; top: 576px; }
  .badge--cut { left: 318px; top: 576px; }
  .weight-rule {
    position: absolute; top: 713px; height: 10px; background: var(--navy);
  }
  .weight-rule--left { left: 0; width: 209px; }
  .weight-rule--right { left: 339px; width: 201px; }
  .net-weight {
    position: absolute; left: 209px; width: 130px; top: 702px;
    text-align: center;
    font-family: "Arimo", sans-serif; font-size: 28px; color: var(--ink);
  }
</style>
</head>
<body>
  <main class="label">
    <header class="brand-band">
      <span class="brand-name">Tidewell Market</span>
    </header>

    <section class="title-box">
      <h1 class="product-name">lobster<br>tails</h1>
      <p class="origin">honduras</p>
    </section>

    <div class="illustration" role="img" aria-label="Navy line drawing of a lobster with claws raised"></div>

    <div class="badges">
      <div class="badge badge--fresh">100%<br>Fresh</div>
      <div class="badge badge--quality">Premium<br>Quality</div>
      <div class="badge badge--cut">Hand Cut<br>Seafood</div>
    </div>

    <div class="weight-rule weight-rule--left"></div>
    <p class="net-weight">5 oz</p>
    <div class="weight-rule weight-rule--right"></div>
  </main>
</body>
</html>
```